Birchway Cleaning Commercial Flyer

Would like a flyer that will be used for making sales calls for commercial clients. These flyers will be handed out to Business Owners and facility managers. The flyer must peak interest, introduce the company, and give some information about our services. Birchway Cleaning Services (BWS) is a modern company that is eco-friendly. I have added what the uniform shirt looks like we have one in orange and one in blue. It would be nice to see the pictures you choose have the uniform on.

Target Market(s)

Office Mangers and Facility managers

Industry/Entity Type

Office Cleaning

Font styles to use
Serif

Colors
f78f20
0355a3
abd037

Requirements
Must have
• Modern clean look and feel. The flyer must straight forward and not busy.
• Have sections where bullet points or other written information can be placed
• Must be able to add and move information myself after the design has been decided on.
• Have a section that says:
• To learn more call 301-555-0148 or email info@birchway-tidyco.example
Nice to have
• Some pictures, clean and modern. Peak interest. The uniform to be photoshopped onto the models of the pictures
Should not have
• too busy

```html
<!DOCTYPE html>
<html lang="en">
<head>
<meta charset="utf-8">
<title>Birchway Cleaning Commercial Flyer</title>
<link href="https://fonts.googleapis.com/css2?family=Open+Sans:ital,wght@0,400;0,600;0,700;0,800;1,600;1,700&display=swap" rel="stylesheet">
<style>
  :root {
    --orange: #f78f20;
    --blue: #0355a3;
    --blue-dark: #023f7c;
    --green: #abd037;
    --ink: #2a2a2a;
    --white: #ffffff;
  }
  * { margin: 0; padding: 0; box-sizing: border-box; }
  html, body { width: 849px; height: 1200px; overflow: hidden; background: #e9ecef; }
  body { font-family: "Open Sans", Arial, sans-serif; color: var(--ink); }
  .flyer { position: relative; width: 849px; height: 1200px; background: var(--white); overflow: hidden; }
  .flyer-shapes { position: absolute; inset: 0; }

  .brand {
    position: absolute; top: 0; right: 40px; width: 230px; height: 120px;
    background: var(--white); border-radius: 0 0 14px 14px;
    display: flex; align-items: center; justify-content: center; gap: 10px;
    box-shadow: 0 3px 8px rgba(0,0,0,.15);
  }
  .brand-mark { width: 22px; height: 22px; border-radius: 50%; background: var(--orange); flex: none; }
  .brand-name { font-weight: 700; font-size: 19px; line-height: 1.15; color: var(--blue); }

  .about { position: absolute; left: 70px; top: 568px; width: 540px; }
  .about-title { font-size: 38px; font-weight: 800; color: var(--blue); letter-spacing: .5px; line-height: 1.2; margin-bottom: 8px; }
  .about-text { font-size: 14.5px; line-height: 1.45; color: #3a3a3a; margin-bottom: 8px; }
  .about-text strong { font-weight: 700; }

  .services { position: absolute; left: 70px; top: 756px; list-style: none; }
  .services li {
    display: flex; align-items: center; gap: 14px;
    color: var(--white); font-style: italic; font-weight: 700; font-size: 21px;
    line-height: 29px; margin-bottom: 11px;
  }
  .services svg { flex: none; }

  .follow { position: absolute; left: 70px; top: 980px; }
  .follow-title { font-size: 32px; font-weight: 800; color: var(--blue); line-height: 1.2; margin-bottom: 14px; }
  .social { display: flex; gap: 14px; }
  .social span { width: 40px; height: 40px; border-radius: 50%; background: #222; display: block; }

  .contact { position: absolute; right: 40px; top: 958px; text-align: right; color: var(--white); }
  .contact-lead { font-size: 26px; font-weight: 700; line-height: 1.15; }
  .contact-phone { font-size: 52px; font-weight: 800; line-height: 1.1; margin-top: 2px; }
  .contact-line { font-size: 17px; font-weight: 600; line-height: 1.45; }
</style>
</head>
<body>
<main class="flyer">
  <svg class="flyer-shapes" width="849" height="1200" viewBox="0 0 849 1200">
    <defs>
      <linearGradient id="photo-tone" x1="0" y1="0" x2="0" y2="1">
        <stop offset="0" stop-color="#f3efe8"/>
        <stop offset=".45" stop-color="#e2cfb5"/>
        <stop offset="1" stop-color="#b98d62"/>
      </linearGradient>
      <linearGradient id="contact-tone" x1="0" y1="0" x2="1" y2="1">
        <stop offset="0" stop-color="#1a8ad8"/>
        <stop offset="1" stop-color="#023f7c"/>
      </linearGradient>
    </defs>

    <rect role="img" aria-label="Photo of a person in pink slippers cleaning a wooden office floor with a green flat mop" x="0" y="0" width="849" height="440" fill="url(#photo-tone)"/>

    <path d="M0 430 C 250 380, 560 360, 849 320 L849 600 L0 600 Z" fill="var(--white)"/>
    <path d="M0 430 C 250 380, 560 360, 849 320" fill="none" stroke="var(--green)" stroke-width="8"/>
    <path d="M0 442 C 250 392, 560 372, 849 332" fill="none" stroke="var(--blue)" stroke-width="4"/>

    <circle cx="190" cy="460" r="94" fill="var(--white)" stroke="var(--green)" stroke-width="6"/>
    <circle role="img" aria-label="Photo of a gloved hand holding a spray bottle" cx="190" cy="460" r="86" fill="#d9dde2"/>
    <circle cx="430" cy="425" r="94" fill="var(--white)" stroke="var(--green)" stroke-width="6"/>
    <circle role="img" aria-label="Photo of a worker with a backpack vacuum" cx="430" cy="425" r="86" fill="#8f959b"/>
    <circle cx="665" cy="390" r="94" fill="var(--white)" stroke="var(--green)" stroke-width="6"/>
    <circle role="img" aria-label="Photo of a stack of colourful microfiber cloths" cx="665" cy="390" r="86" fill="#d9a3b8"/>

    <path d="M0 732 L660 732 C 750 732, 800 745, 849 702 L849 938 L0 938 Z" fill="var(--orange)"/>

    <path d="M280 1200 C 290 1000, 420 930, 849 905 L849 1200 Z" fill="url(#contact-tone)"/>
    <path d="M0 1165 C 300 1185, 560 1172, 849 1148 L849 1166 C 560 1190, 300 1200, 0 1184 Z" fill="var(--green)"/>
    <path d="M0 1184 C 300 1200, 560 1190, 849 1166 L849 1200 L0 1200 Z" fill="var(--blue)"/>
  </svg>

  <div class="brand">
    <span class="brand-mark"></span>
    <span class="brand-name">Birchway Cleaning<br>Services</span>
  </div>

  <section class="about">
    <h2 class="about-title">ABOUT US</h2>
    <p class="about-text"><strong>We at Birchway Cleaning Services have one mission – to provide our clients the absolute best service available in the industry.</strong></p>
    <p class="about-text">This is done through providing timely, efficient, thoughtful, and thorough service. This is what we call “The Royal Treatment.”</p>
  </section>

  <ul class="services">
    <li><svg width="22" height="18" viewBox="0 0 22 18"><path d="M2 9 L8 15 L20 2" fill="none" stroke="#abd037" stroke-width="4"/></svg>Hospital Grade disinfectants</li>
    <li><svg width="22" height="18" viewBox="0 0 22 18"><path d="M2 9 L8 15 L20 2" fill="none" stroke="#abd037" stroke-width="4"/></svg>Eco-Friendly- microfiber cloths</li>
    <li><svg width="22" height="18" viewBox="0 0 22 18"><path d="M2 9 L8 15 L20 2" fill="none" stroke="#abd037" stroke-width="4"/></svg>HEPA Backpack Vacuums</li>
    <li><svg width="22" height="18" viewBox="0 0 22 18"><path d="M2 9 L8 15 L20 2" fill="none" stroke="#abd037" stroke-width="4"/></svg>Microfiber No Dip Mopping System</li>
  </ul>

  <section class="follow">
    <h3 class="follow-title">Follow Us at</h3>
    <div class="social"><span></span><span></span><span></span></div>
  </section>

  <section class="contact">
    <p class="contact-lead">Contact Us<br>for a Free Quote</p>
    <p class="contact-phone">301.555.0148</p>
    <p class="contact-line">info@birchway-tidyco.example</p>
    <p class="contact-line">www.birchway-tidyco.example</p>
  </section>
</main>
</body>
</html>
```